Veltarum

Standard Business Card design.
Sample two-sided design uploaded. White front, Black back.
Would like white shield to be on all black background side.
Willing to look at a couple creative designs, but nothing crazy.
Preference for a classic, confident, strong design.

```html
<!DOCTYPE html>
<html lang="en">
<head>
<meta charset="utf-8">
<title>Veltarum Business Card</title>
<link rel="stylesheet" href="https://fonts.googleapis.com/css2?family=Questrial&display=swap">
<style>
  :root {
    --backdrop: #ededed;
    --card-white: #ffffff;
    --card-black: #000000;
    --ink: #111111;
    --silver: #c8c8c8;
  }
  * { margin: 0; padding: 0; box-sizing: border-box; }
  html, body {
    width: 1200px;
    height: 1200px;
    overflow: hidden;
    background: var(--backdrop);
    font-family: "Questrial", sans-serif;
  }
  .canvas {
    position: relative;
    width: 1200px;
    height: 1200px;
  }
  .card {
    position: absolute;
    left: 150px;
    width: 902px;
    height: 528px;
    overflow: hidden;
  }
  .card-front { top: 54px; background: var(--card-white); color: var(--ink); }
  .card-back { top: 625px; background: var(--card-black); }

  .accent-bar {
    position: absolute;
    left: 790px;
    width: 44px;
    background: var(--card-black);
  }
  .accent-bar-top { top: 0; height: 190px; }
  .accent-bar-bottom { bottom: 0; height: 34px; }

  .brand {
    position: absolute;
    display: flex;
    align-items: center;
    gap: 16px;
    font-size: 50px;
    letter-spacing: 4px;
    text-transform: uppercase;
    line-height: 1;
  }
  .brand-mark { width: 22px; height: 22px; flex: none; }
  .card-front .brand { left: 84px; top: 208px; color: var(--ink); }
  .card-front .brand-mark { background: var(--ink); }
  .card-back .brand {
    left: 50%;
    top: 50%;
    transform: translate(-50%, -50%);
    color: var(--silver);
    font-size: 66px;
    letter-spacing: 6px;
  }
  .card-back .brand-mark { background: var(--silver); width: 28px; height: 28px; }

  .holder-name {
    position: absolute;
    right: 68px;
    top: 254px;
    font-size: 41px;
    line-height: 1;
  }
  .contact-list {
    position: absolute;
    right: 68px;
    top: 346px;
    list-style: none;
    font-size: 21px;
    line-height: 1;
  }
  .contact-item {
    display: flex;
    justify-content: flex-end;
    align-items: center;
    gap: 14px;
    height: 36px;
  }
  .contact-icon { width: 15px; height: 15px; flex: none; }
</style>
</head>
<body>
<main class="canvas">

  <section class="card card-front" aria-label="Business card front">
    <div class="accent-bar accent-bar-top"></div>
    <div class="accent-bar accent-bar-bottom"></div>

    <div class="brand"><span class="brand-mark"></span>Veltarum</div>

    <h1 class="holder-name">Mara Lindqvist</h1>

    <ul class="contact-list">
      <li class="contact-item">
        <span>000-418-0000</span>
        <svg class="contact-icon" viewBox="0 0 16 16" aria-hidden="true">
          <path d="M3.5 1.5l2.5 2.6-1.3 1.7c.9 2 2.4 3.6 4.5 4.6l1.7-1.3 2.6 2.5-1.4 2.2C7 13.5 2.6 9 1.4 3z" fill="var(--ink)"/>
        </svg>
      </li>
      <li class="contact-item">
        <span>mara@veltarum.com</span>
        <svg class="contact-icon" viewBox="0 0 16 16" aria-hidden="true">
          <rect x="1" y="3" width="14" height="10" fill="var(--ink)"/>
          <path d="M1.5 3.5L8 9l6.5-5.5" fill="none" stroke="#fff" stroke-width="1.2"/>
        </svg>
      </li>
      <li class="contact-item">
        <span>www.veltarum.com</span>
        <svg class="contact-icon" viewBox="0 0 16 16" aria-hidden="true">
          <circle cx="8" cy="8" r="6.5" fill="none" stroke="var(--ink)" stroke-width="1.6"/>
          <ellipse cx="8" cy="8" rx="2.8" ry="6.5" fill="none" stroke="var(--ink)" stroke-width="1.2"/>
          <path d="M1.5 8h13" stroke="var(--ink)" stroke-width="1.2"/>
        </svg>
      </li>
    </ul>
  </section>

  <section class="card card-back" aria-label="Business card back">
    <div class="brand"><span class="brand-mark"></span>Veltarum</div>
  </section>

</main>
</body>
</html>
```